Harbor Business Cards

I need a business card designed with the following information.

Company Name: Harbor Wealth Management
Name: BriAnne Dockery
Title: Executive Assistant
Cell: (409) 555-0173
Direct Line: (512) 555-0148
Email: brianne@harborwmx.com
Address: 20537 W. Marlowe PKWY Ste. B
Lakemont, NV 77390

I have attached the logo.
I would like it in navy blue and silver.
Thanks.

```html
<!DOCTYPE html>
<html lang="en">
<head>
<meta charset="utf-8">
<title>Harbor Wealth Management – Business Card</title>
<link rel="stylesheet" href="https://fonts.googleapis.com/css2?family=Work+Sans:wght@400;700&display=swap">
<style>
  :root {
    --navy: #14264a;
    --navy-deep: #0f1f3d;
    --silver: #c9ced6;
    --ink-muted: #6b7280;
    --paper: #ffffff;
    --backdrop: #a9a9ab;
    --scene-top: #3b4f78;
    --scene-mid: #2e4a45;
    --scene-low: #24382f;
  }
  * { margin: 0; padding: 0; box-sizing: border-box; }
  html, body { width: 1200px; height: 930px; overflow: hidden; }
  body {
    background: var(--backdrop);
    font-family: "Work Sans", Arial, sans-serif;
    position: relative;
  }
  .card {
    position: absolute;
    width: 640px;
    height: 366px;
    border-radius: 22px;
    overflow: hidden;
  }
  .card--front { left: 110px; top: 60px; }
  .card--back  { left: 450px; top: 500px; background: var(--paper); }

  .front-photo {
    position: absolute; inset: 0;
    background: linear-gradient(170deg, var(--scene-top) 0%, var(--scene-mid) 55%, var(--scene-low) 100%);
  }
  .front-brand {
    position: absolute; left: 0; right: 0; top: 150px;
    text-align: center; color: var(--paper); font-weight: 400;
  }
  .front-brand .brand-name { font-size: 40px; letter-spacing: 14px; }
  .front-brand .brand-sub  { font-size: 13px; letter-spacing: 4px; margin-top: 6px; }

  .back-brand {
    position: absolute; right: 38px; top: 70px;
    text-align: right; color: var(--navy); font-weight: 400;
  }
  .back-brand .brand-name { font-size: 30px; letter-spacing: 10px; }
  .back-brand .brand-sub  { font-size: 10px; letter-spacing: 3px; margin-top: 4px; }

  .rule { position: absolute; height: 1px; background: var(--navy); }
  .rule--top { left: 230px; right: 36px; top: 140px; }
  .rule--mid { left: 40px; width: 250px; top: 236px; }

  .person { position: absolute; left: 40px; top: 170px; }
  .person .name { font-size: 26px; font-weight: 700; color: var(--navy); letter-spacing: 1px; }
  .person .title { font-size: 15px; color: var(--ink-muted); margin-top: 2px; }

  .address {
    position: absolute; right: 36px; top: 156px;
    text-align: right; font-size: 15px; color: var(--ink-muted); line-height: 1.35;
  }

  .contacts { position: absolute; left: 40px; top: 246px; list-style: none; }
  .contacts li {
    display: flex; align-items: center; gap: 8px;
    font-size: 15px; color: var(--ink-muted); line-height: 23px;
  }
  .contacts svg { width: 12px; height: 12px; fill: var(--navy); flex: none; }

  .wave { position: absolute; left: 0; bottom: 0; width: 640px; height: 366px; }
</style>
</head>
<body>
  <section class="card card--front">
    <div class="front-photo" role="img" aria-label="Mountain valley landscape photograph with a winding river under a cloudy sky, tinted navy"></div>
    <div class="front-brand">
      <div class="brand-name">HARBOR</div>
      <div class="brand-sub">WEALTH MANAGEMENT</div>
    </div>
  </section>

  <section class="card card--back">
    <svg class="wave" viewBox="0 0 640 366" aria-hidden="true">
      <path d="M0,366 C300,366 440,330 640,246 L640,366 Z" fill="var(--navy-deep)"/>
      <path d="M180,366 C360,360 470,326 640,238" fill="none" stroke="var(--silver)" stroke-width="3"/>
      <path d="M240,366 C380,356 480,322 640,230" fill="none" stroke="var(--navy)" stroke-width="2"/>
    </svg>

    <div class="back-brand">
      <div class="brand-name">HARBOR</div>
      <div class="brand-sub">WEALTH MANAGEMENT</div>
    </div>
    <div class="rule rule--top"></div>

    <div class="address">
      <p>20537 W. Marlowe PKWY Ste. B</p>
      <p>Lakemont, NV 77390</p>
    </div>

    <div class="person">
      <p class="name">BRIANNE DOCKERY</p>
      <p class="title">Executive Assistant</p>
    </div>
    <div class="rule rule--mid"></div>

    <ul class="contacts">
      <li><svg viewBox="0 0 12 12"><path d="M2.5 0.8 L4.3 2.8 L3.4 4.3 C4 5.8 6.2 8 7.7 8.6 L9.2 7.7 L11.2 9.5 L10 11.2 C5.5 11 1 6.5 0.8 2 Z"/></svg>(512) 555-0148</li>
      <li><svg viewBox="0 0 12 12"><path d="M3 0 H9 A1 1 0 0 1 10 1 V11 A1 1 0 0 1 9 12 H3 A1 1 0 0 1 2 11 V1 A1 1 0 0 1 3 0 Z M3.5 1.5 V9.5 H8.5 V1.5 Z"/></svg>(409) 555-0173</li>
      <li><svg viewBox="0 0 12 12"><path d="M0 2 H12 V10 H0 Z M1.2 3.2 V8.8 H10.8 V3.2 L6 6.6 Z M1.8 3 L6 5.8 L10.2 3 Z"/></svg>brianne@harborwmx.com</li>
      <li><svg viewBox="0 0 12 12"><circle cx="6" cy="6" r="6"/></svg>www.harborwmx.com</li>
    </ul>
  </section>
</body>
</html>
```